Premium Epoxy Distributor Needs Landing Page Design and Copy Writing

We need a high converting landing page with full service design and copy writing for our search engine marketing campaign. We are the exclusive distributor for a US manufacturer of high quality, industrial grade garage floor epoxies. Our primarily market is the DIY (do-it-yourself) within the US. Our unique selling proposition is that we are able to provide industrial grade epoxies to the public which were only available to contractors and professional installers before.

The final design should be modern, sleek and visually appealing. The copy writing should be clear and succinct, and communicate the benefits of our product and tailored for the DIY market.

We have not chosen a land page platform, but were looking at Shogun or Unbounce.

Target Market(s)

Garage Floor Epoxy market with a concentrated focus on the DIYer (Do It Yourself).
Home improvement market.

Requirements
Must have
• Excellent copy writing, someone who is familiar with the home improvement market, garage floor epoxies or the coatings industry is a plus.
Nice to have
• We have invested heavily into a custom product configurator which provides real time pricing for each individual project based on square footage. If you think this is something of value please add it to the landing page content.

```html
<!DOCTYPE html>
<html lang="en">
<head>
<meta charset="utf-8">
<title>Ironclad Coatings – Industrial-Grade Garage Floor Epoxy for DIYers</title>
<link href="https://fonts.googleapis.com/css2?family=Montserrat:wght@400;500;600&family=Lora:wght@400&display=swap" rel="stylesheet">
<style>
:root{
  --red:#e8262d;
  --ink:#151515;
  --muted:#6b6b6b;
  --soft:#f4f4f4;
  --white:#ffffff;
  --teal:#0f5f57;
}
*{box-sizing:border-box;margin:0;padding:0}
html,body{width:1200px;height:3693px;overflow:hidden}
body{font-family:"Lora",Georgia,serif;color:var(--ink);background:var(--white)}
section,footer{position:relative;width:1200px;overflow:hidden}
.abs{position:absolute}
.head{font-family:"Montserrat",Arial,sans-serif}
.btn{font-family:"Montserrat",Arial,sans-serif;font-weight:500;font-size:18px;color:var(--white);background:var(--red);border-radius:28px;display:flex;align-items:center;justify-content:center;text-decoration:none}

.hero{height:695px;background:linear-gradient(100deg,#d9d9d7 0%,#bdbcb8 35%,#6e6b66 62%,#3c3935 100%)}
.hero-photo{left:540px;top:0;width:660px;height:695px;background:radial-gradient(ellipse at 55% 55%,#8a8884 0%,#55524d 55%,#2e2b28 100%);opacity:.85}
.brand{left:89px;top:46px;font-family:"Montserrat",sans-serif;font-weight:600;font-size:28px;color:var(--red);display:flex;align-items:center;gap:10px}
.brand i{width:16px;height:16px;border-radius:50%;background:var(--red);display:block}
.menu{left:1092px;top:42px}
.hero-title{left:89px;top:180px;font-size:70px;font-weight:500;line-height:70px}
.hero-sub{left:89px;top:342px;width:480px;font-size:23px;line-height:35px}
.hero .btn{left:89px;top:441px;width:192px;height:55px}

.welcome{height:642px}
.welcome h2{position:absolute;top:100px;width:100%;text-align:center;font-size:40px;font-weight:500}
.welcome p.lead{position:absolute;left:145px;top:172px;width:910px;text-align:center;font-size:17px;line-height:32px;color:var(--muted)}
.benefit{position:absolute;top:340px;width:260px;text-align:center}
.benefit svg{display:block;margin:0 auto}
.benefit h3{font-family:"Montserrat",sans-serif;font-weight:500;font-size:22px;margin-top:28px}
.benefit p{font-size:15px;line-height:25px;color:var(--muted);margin-top:14px}

.testimonial{height:613px;background:linear-gradient(90deg,#3a1e10 0%,#7a4424 35%,#8a5030 55%,#5a301a 80%,#2e180c 100%);color:var(--white);text-align:center}
.testimonial h2{position:absolute;top:104px;width:100%;font-size:22px;font-weight:500}
.quote-mark{left:585px;top:178px}
.testimonial blockquote{position:absolute;left:120px;top:228px;width:960px;font-family:"Montserrat",sans-serif;font-size:23px;line-height:38px}
.avatar{left:552px;top:372px;width:96px;height:96px;border-radius:50%;background:linear-gradient(#c9c2ba,#8f877f);border:2px solid #d8d8d8}
.customer{position:absolute;top:482px;width:100%;font-family:"Montserrat",sans-serif;font-weight:500;font-size:16px}
.stars{position:absolute;top:514px;width:100%;color:#f2c200;font-size:11px;letter-spacing:1px}

.features{height:598px;background:var(--soft)}
.feature{position:absolute;top:103px;width:334px;text-align:center}
.feature .ph{height:224px}
.feature h3{font-family:"Montserrat",sans-serif;font-weight:500;font-size:22px;margin-top:26px}
.feature p{font-size:15.5px;line-height:26px;color:var(--muted);margin:12px 18px 0}

.what{height:640px}
.what-photo{left:201px;top:111px;width:388px;height:415px;background:linear-gradient(160deg,#5d8a5c 0%,#c9d3cc 45%,#eceeed 70%,#a9c4b3 100%)}
.what h2{left:640px;top:158px;font-size:40px;font-weight:500;line-height:46px}
.what p{left:640px;top:282px;width:360px;font-size:17px;line-height:30px;color:var(--muted);text-align:justify}

.contact{height:454px;background:linear-gradient(170deg,#2a1a12 0%,#0f4d47 30%,var(--teal) 50%,#0c3f3a 68%,#3a2317 100%);color:var(--white);text-align:center}
.contact h2{position:absolute;top:130px;width:100%;font-size:40px;font-weight:500}
.contact p{position:absolute;left:290px;top:196px;width:620px;font-size:17px;line-height:26px}
.contact .btn{left:503px;top:270px;width:193px;height:55px}

footer{height:51px;text-align:center;font-size:10px;color:var(--muted);padding-top:19px}
</style>
</head>
<body>

<section class="hero">
  <div class="abs hero-photo" role="img" aria-label="Worker running a floor grinder across a concrete floor"></div>
  <div class="abs brand"><i></i>IRONCLAD COATINGS</div>
  <svg class="abs menu" width="18" height="16" viewBox="0 0 18 16"><rect y="1" width="18" height="3" fill="#fff"/><rect y="7" width="18" height="3" fill="#fff"/><rect y="13" width="18" height="3" fill="#fff"/></svg>
  <h1 class="abs head hero-title">Ironclad<br>Coatings</h1>
  <p class="abs head hero-sub">Pro-grade garage floor epoxy, now sold direct to do-it-yourselfers</p>
  <a class="abs btn" href="#">Price My Floor</a>
</section>

<section class="welcome">
  <h2 class="head">Welcome To Ironclad Coatings</h2>
  <p class="lead">For years, true industrial-grade garage floor epoxy was sold only to contractors and professional installers. As the exclusive distributor for a leading US manufacturer, we now ship that same pro system straight to your door, so you can lay a showroom-tough floor yourself in one weekend and skip the installer bill.</p>
  <div class="benefit" style="left:150px">
    <svg width="84" height="60" viewBox="0 0 84 60" fill="none" stroke="#e8262d" stroke-width="3"><rect x="4" y="22" width="22" height="22"/><rect x="58" y="22" width="22" height="22"/><rect x="32" y="6" width="20" height="48"/><line x1="2" y1="52" x2="82" y2="52"/></svg>
    <h3>Contractor Grade</h3>
    <p>The same 100% solids epoxy the pros use, built to shrug off hot tires, oil, salt and dropped tools for years.</p>
  </div>
  <div class="benefit" style="left:470px">
    <svg width="64" height="60" viewBox="0 0 64 60" fill="none" stroke="#e8262d" stroke-width="3"><circle cx="20" cy="14" r="9"/><rect x="6" y="26" width="28" height="28"/><rect x="38" y="20" width="20" height="34"/><line x1="2" y1="56" x2="62" y2="56"/></svg>
    <h3>Made For DIY</h3>
    <p>Pre-measured kits, clear step-by-step guides and real support mean no guesswork, even on your first floor.</p>
  </div>
  <div class="benefit" style="left:791px">
    <svg width="58" height="60" viewBox="0 0 58 60" fill="none" stroke="#e8262d" stroke-width="3"><line x1="4" y1="4" x2="54" y2="4"/><rect x="12" y="14" width="14" height="14"/><rect x="32" y="26" width="14" height="14"/><rect x="4" y="46" width="50" height="10" rx="5"/></svg>
    <h3>Instant Pricing</h3>
    <p>Enter your square footage in our configurator and see an exact price for your whole project in real time.</p>
  </div>
</section>

<section class="testimonial" role="img" aria-label="Dark wood plank background">
  <h2 class="head">What Our Customers Say</h2>
  <svg class="abs quote-mark" width="30" height="18" viewBox="0 0 30 18"><path d="M2 18V9C2 4 5 1 10 0v4c-3 1-4 3-4 5h5v9zM18 18V9c0-5 3-8 8-9v4c-3 1-4 3-4 5h5v9z" fill="#e8262d"/></svg>
  <blockquote>I priced my two-car garage online in under a minute, had the kit on my porch that week and finished the floor over a Saturday. Two winters of salt and snow later, it still looks like the day I rolled it out.</blockquote>
  <div class="abs avatar" role="img" aria-label="Customer portrait"></div>
  <div class="customer">Dana Miller</div>
  <div class="stars">★★★★★</div>
</section>

<section class="features">
  <div class="feature" style="left:89px">
    <div class="ph" role="img" aria-label="Yellow epoxy being poured onto a floor" style="background:linear-gradient(135deg,#e3c06a,#c99a3c)"></div>
    <h3>Thick, Glossy Finish</h3>
    <p>A high-build coat that levels itself into a deep, glass-like shine and hides hairline cracks in old concrete.</p>
  </div>
  <div class="feature" style="left:434px">
    <div class="ph" role="img" aria-label="Craftsman working in a wood shop" style="background:linear-gradient(135deg,#8a6a4a,#3c2e24)"></div>
    <h3>Everything In The Box</h3>
    <p>Etch, primer, epoxy, color flakes and topcoat, sized to your floor so you never run short mid-pour.</p>
  </div>
  <div class="feature" style="left:778px">
    <div class="ph" role="img" aria-label="Hands polishing a wood and blue resin table" style="background:linear-gradient(135deg,#6d5443,#b07a3e 55%,#3d7f93)"></div>
    <h3>Price Your Floor</h3>
    <p>Choose size, color and finish in our configurator and watch your total update live before you order.</p>
  </div>
</section>

<section class="what">
  <div class="abs what-photo" role="img" aria-label="Gloved hand spreading epoxy with a trowel"></div>
  <h2 class="abs head">What We<br>Do</h2>
  <p class="abs">We put industrial epoxy in the hands of homeowners. Every kit comes from one US manufacturer, is matched to your square footage, and ships with the same prep and coating steps the pros follow, so your garage gets a floor that lasts.</p>
</section>

<section class="contact" role="img" aria-label="Dark wood slab with teal resin river">
  <h2 class="head">Get Your Price</h2>
  <p>Tell us your garage size and see your exact project cost in seconds. Questions? Our coating experts are a call away.</p>
  <a class="abs btn" href="#">Start Now</a>
</section>

<footer>© 2020 Ironclad Coatings. All Rights Reserved</footer>

</body>
</html>
```